Иллюстрация для Подарочный квартальный производственный календарь
Задание на дизайн
Где будет использоваться иллюстрация?
Подарочный календарь для клиентов типографии
Добрый день.
Требуется отрисовать макет для квартального календаря на 2025 год. Календарь будет подарочным для клиентов компании “Дом Листов”. Календарь состоит из:
Верхнего блока (шапки), который должен быть в двух вариантах: 1) Общий вариант с красивым дизайном; 2) Вариант с этим же дизайном и местом, куда можно будет вставить логотип компании, которой этот календарь будет отправлен.
Размер 250 на 370 миллиметров
Индивидуальные блоки: 14 календарных листов: на каждый месяц 2025 года, декабрь 2024 года и январь 2026 года.
Размер 160 на 355 миллиметров
Ламинированные подложки под календарные блоки: на первой под календарным блоком будет располагаться девиз, на второй - мотивирующая фраза, на третьей - информация о компании “Дом Листов” - Логотип, наименование, адрес, телефон и email.
Правила по стилистике:
Календарные листы с абстрактным дизайном, рабочие дни должны быть черного цвета, а выходные и праздничные дни корпоративного цвета, HEX-код: #41ae62
Для верхнего блока необходимо придумать тематический дизайн. Можно использовать идею о годе змеи, которым будет 2025 год, также можно выделить определенные детали для фольгирования.
Приветствуются ваши идеи для девиза и мотивирующей надписи.
Требования к готовым файлам:
Нам необходимы будут готовые для печати файлы в форматах .ai или .cdr с вылетами и цветами CMYK. В приложение к этому нам нужны будут файлы в форматах .png и .pdf
О компании:
Для понимания специфики, наша компания “Дом Листов” специализируется на цифровой печати многополосных изделий: книг, журналов, блокнотов и так далее. Сайт компании выполнен в минималистичном стиле: https://listodom-studio.ru/
В планировании дизайна не обязательно пользоваться минималистичными формами, главное, чтобы это было красиво и не пошло.
Наименование компании: ООО «ДОМ ЛИСТОВ»
Адрес: 129344, г. Москва, Зелёный 5-й переулок, дом 17, строение 2, офис 14
Телефон: +7 (916) 457-31-09
Email: mv@listodom-studio.ru
Приложения:
В приложениях представлен пример календаря для понимания его измерений и блоков. Также в приложении логотип компании “Дом Листов”
ТЗ на гуглдоксе:
https://docs.example-notes.com/document/d/7QxLmT3pWz9kRb2NvYc4HsJdFg8AeUoKtPiZr5MwQnE/edit?usp=sharing

```html
<!DOCTYPE html>
<html lang="ru">
<head>
<meta charset="utf-8">
<title>Квартальный календарь 2025 — Дом Листов</title>
<link rel="stylesheet" href="https://fonts.googleapis.com/css2?family=Open+Sans:ital,wght@0,300;0,400;0,600;0,700;1,300;1,400&display=swap">
<style>
  :root{
    --page:#ffffff;
    --ink:#111111;
    --brand:#41ae62;
    --brand-soft:#a9d9b7;
    --muted:#b3b3b3;
    --week:#6f6f6f;
    --rule:#cfcfcf;
    --head-band:#e6f3ea;
    --scale-tone:#d9efdf;
    --white:#ffffff;
    --ring:#9a9a9a;
  }
  *{box-sizing:border-box;margin:0;padding:0}
  html,body{width:1200px;height:848px;overflow:hidden;background:var(--page)}
  body{position:relative;font-family:"Open Sans",sans-serif;color:var(--ink)}

  .calendar{position:absolute;left:450px;top:19px;width:300px;height:810px;overflow:hidden;background:#173a2a}
  .backdrop{position:absolute;inset:0;width:300px;height:810px;display:block}
  .hang-hole{position:absolute;left:148px;top:7px;width:5px;height:5px;border-radius:50%;background:#f3d9de}

  .year{position:absolute;left:11px;top:2px;font-weight:700;font-size:49px;line-height:1.1;color:var(--white);letter-spacing:-1px}
  .client-logo{position:absolute;left:222px;top:10px;color:#7f8c86;font-weight:300}
  .client-logo .word{font-size:15px;line-height:15px;letter-spacing:.4px}
  .client-logo .sub{font-size:6px;line-height:7px;letter-spacing:.4px}
  .motto{position:absolute;right:12px;top:48px;text-align:right;color:var(--white);font-style:italic;font-weight:300;font-size:14px;line-height:20px}

  .sheet{position:absolute;left:6px;width:288px;height:129px;background:var(--white)}
  .sheet.dec{top:203px}.sheet.jan{top:406px}.sheet.feb{top:608px}
  .binding{position:absolute;left:14px;right:6px;top:-9px;height:13px;
    background:repeating-linear-gradient(90deg, transparent 0 1px, var(--ring) 1px 3px, transparent 3px 6.3px);border-radius:2px}
  .binding::after{content:"";position:absolute;left:0;right:0;top:9px;height:2px;background:rgba(80,80,80,.5)}
  .scales{position:absolute;top:0;bottom:0;width:44px;background:var(--scale-tone)}
  .dec .scales,.feb .scales{left:0;border-radius:0 22px 22px 0}
  .jan .scales{right:0;border-radius:22px 0 0 22px}

  .grid{position:absolute;top:0;width:231px}
  .dec .grid,.feb .grid{left:51px}
  .jan .grid{left:6px}
  .title{position:absolute;top:11px;left:0;right:0;font-size:8px;line-height:10px;font-weight:400}
  .title b{font-weight:700}
  .title .yr{position:absolute;right:0;font-weight:700}
  .head{position:absolute;top:27px;left:0;right:0;height:13px;background:var(--head-band);display:grid;grid-template-columns:22px repeat(7,1fr)}
  .head span{font-size:3.6px;line-height:4.5px;text-align:center;padding-top:1.5px;font-weight:700;color:#333}
  .head span i{display:block;font-style:normal;font-weight:400;color:#888}
  .rows{position:absolute;top:42px;left:0;right:0}
  .row{display:grid;grid-template-columns:22px repeat(7,1fr);height:16.8px;align-items:center;border-bottom:.6px solid var(--rule)}
  .row:last-child{border-bottom:0}
  .row span{text-align:center;font-size:13px;font-weight:600;line-height:1}
  .row .wk{font-size:9px;color:var(--week);border-right:.8px solid var(--rule);height:100%;display:flex;align-items:center;justify-content:center}
  .row .off{color:var(--brand)}
  .row .other{color:var(--muted);font-weight:400;font-size:10px}
  .row .next{color:var(--brand-soft);font-weight:400;font-size:10px}
  .row .pair{font-size:9px;font-weight:600;white-space:nowrap}
  .row .pair sup{font-size:8px;vertical-align:3px}

  .footer-info{position:absolute;left:94px;top:770px;color:#b9c7bf;font-size:3.6px;line-height:5px;font-weight:400}
  .studio{position:absolute;left:173px;top:769px;display:flex;align-items:center;gap:6px}
  .studio .mark{width:24px;height:24px;border:1px solid var(--white)}
  .studio .name{color:var(--white);font-weight:300;font-size:11.5px;line-height:1;letter-spacing:.3px}
  .studio .tag{display:block;color:var(--white);font-weight:300;font-size:4.6px;letter-spacing:2.4px;margin-top:3px}
</style>
</head>
<body>
<div class="calendar">
  <svg class="backdrop" viewBox="0 0 300 810" role="img" aria-label="Фотоиллюстрация к году змеи: зелёная змея с головой на красной книге, её чешуйчатое тело изгибается вниз по тёмно-зелёному фону с коричневыми бликами">
    <defs>
      <linearGradient id="bg-base" x1="0" y1="0" x2="0" y2="1">
        <stop offset="0" stop-color="#0b2219"/>
        <stop offset=".45" stop-color="#16392a"/>
        <stop offset=".75" stop-color="#1b4a31"/>
        <stop offset="1" stop-color="#1f4f34"/>
      </linearGradient>
      <radialGradient id="glow-green" cx=".5" cy=".5" r=".5">
        <stop offset="0" stop-color="#a9cf8e"/>
        <stop offset=".5" stop-color="#5f9a58"/>
        <stop offset="1" stop-color="#2f6b3c" stop-opacity="0"/>
      </radialGradient>
      <linearGradient id="band-red" x1="0" y1="0" x2="1" y2="0">
        <stop offset="0" stop-color="#8e2a22"/>
        <stop offset=".7" stop-color="#a33a2a"/>
        <stop offset="1" stop-color="#d9c9a4"/>
      </linearGradient>
      <radialGradient id="glow-rust" cx=".5" cy=".5" r=".5">
        <stop offset="0" stop-color="#8a3a14"/>
        <stop offset="1" stop-color="#6b2e14" stop-opacity="0"/>
      </radialGradient>
      <linearGradient id="sheen" x1="0" y1="0" x2="1" y2="1">
        <stop offset="0" stop-color="#2c6a3d" stop-opacity="0"/>
        <stop offset=".5" stop-color="#5c9a62"/>
        <stop offset="1" stop-color="#1d4a2e" stop-opacity="0"/>
      </linearGradient>
      <filter id="soft" x="-30%" y="-30%" width="160%" height="160%"><feGaussianBlur stdDeviation="6"/></filter>
      <filter id="softer" x="-40%" y="-40%" width="180%" height="180%"><feGaussianBlur stdDeviation="12"/></filter>
    </defs>
    <rect width="300" height="810" fill="url(#bg-base)"/>
    <ellipse cx="240" cy="370" rx="90" ry="80" fill="url(#glow-rust)" filter="url(#softer)"/>
    <rect x="0" y="168" width="250" height="34" rx="4" fill="url(#band-red)" filter="url(#soft)" opacity=".9"/>
    <ellipse cx="110" cy="125" rx="85" ry="42" fill="url(#glow-green)" filter="url(#soft)"/>
    <ellipse cx="255" cy="175" rx="35" ry="40" fill="#3f7e63" filter="url(#softer)" opacity=".8"/>
    <ellipse cx="150" cy="375" rx="140" ry="30" fill="url(#sheen)" filter="url(#soft)" transform="rotate(-8 150 375)"/>
    <ellipse cx="200" cy="575" rx="120" ry="26" fill="url(#sheen)" filter="url(#soft)" transform="rotate(6 200 575)"/>
    <ellipse cx="50" cy="795" rx="55" ry="12" fill="#3d7a52" filter="url(#soft)" opacity=".7"/>
  </svg>
  <div class="hang-hole"></div>

  <div class="year">2025</div>
  <div class="client-logo"><div class="word">ЛОГОТИП</div><div class="sub">КОМПАНИЙ</div></div>
  <div class="motto">ВАШИ ИДЕИ, НАША<br>РЕАЛИЗАЦИЯ</div>

  <section class="sheet dec">
    <div class="binding"></div>
    <div class="scales" role="img" aria-label="Декоративный узор змеиной чешуи"></div>
    <div class="grid">
      <div class="title"><b>ДЕКАБРЬ</b>/DECEMBER<span class="yr">2024</span></div>
      <div class="head"><span>Неделя<i>Week</i></span><span>Понедельник<i>Monday</i></span><span>Вторник<i>Tuesday</i></span><span>Среда<i>Wednesday</i></span><span>Четверг<i>Thursday</i></span><span>Пятница<i>Friday</i></span><span>Суббота<i>Saturday</i></span><span>Воскресенье<i>Sunday</i></span></div>
      <div class="rows">
        <div class="row"><span class="wk">49</span><span class="other">25</span><span class="other">26</span><span class="other">27</span><span class="other">28</span><span class="other">29</span><span class="other">30</span><span class="off">1</span></div>
        <div class="row"><span class="wk">50</span><span>2</span><span>3</span><span>4</span><span>5</span><span>6</span><span class="off">7</span><span class="off">8</span></div>
        <div class="row"><span class="wk">51</span><span>9</span><span>10</span><span>11</span><span>12</span><span>13</span><span class="off">14</span><span class="off">15</span></div>
        <div class="row"><span class="wk">52</span><span>16</span><span>17</span><span>18</span><span>19</span><span>20</span><span class="off">21</span><span class="off">22</span></div>
        <div class="row"><span class="wk">01</span><span class="pair"><sup>23</sup>/30</span><span class="pair"><sup>24</sup>/<span class="off">31</span></span><span>25</span><span>26</span><span>27</span><span class="off">28</span><span class="off">29</span></div>
      </div>
    </div>
  </section>

  <section class="sheet jan">
    <div class="binding"></div>
    <div class="scales" role="img" aria-label="Декоративный узор змеиной чешуи"></div>
    <div class="grid">
      <div class="title"><b>ЯНВАРЬ</b>/JANUARY<span class="yr">2025</span></div>
      <div class="head"><span>Неделя<i>Week</i></span><span>Понедельник<i>Monday</i></span><span>Вторник<i>Tuesday</i></span><span>Среда<i>Wednesday</i></span><span>Четверг<i>Thursday</i></span><span>Пятница<i>Friday</i></span><span>Суббота<i>Saturday</i></span><span>Воскресенье<i>Sunday</i></span></div>
      <div class="rows">
        <div class="row"><span class="wk">01</span><span class="other">30</span><span class="next">31</span><span class="off">1</span><span class="off">2</span><span class="off">3</span><span class="off">4</span><span class="off">5</span></div>
        <div class="row"><span class="wk">02</span><span class="off">6</span><span class="off">7</span><span class="off">8</span><span>9</span><span>10</span><span class="off">11</span><span class="off">12</span></div>
        <div class="row"><span class="wk">03</span><span>13</span><span>14</span><span>15</span><span>16</span><span>17</span><span class="off">18</span><span class="off">19</span></div>
        <div class="row"><span class="wk">04</span><span>20</span><span>21</span><span>22</span><span>23</span><span>24</span><span class="off">25</span><span class="off">26</span></div>
        <div class="row"><span class="wk">05</span><span>27</span><span>28</span><span>29</span><span>30</span><span>31</span><span class="next">1</span><span class="next">2</span></div>
      </div>
    </div>
  </section>

  <section class="sheet feb">
    <div class="binding"></div>
    <div class="scales" role="img" aria-label="Декоративный узор змеиной чешуи"></div>
    <div class="grid">
      <div class="title"><b>ФЕВРАЛЬ</b>/FEBRUARY<span class="yr">2025</span></div>
      <div class="head"><span>Неделя<i>Week</i></span><span>Понедельник<i>Monday</i></span><span>Вторник<i>Tuesday</i></span><span>Среда<i>Wednesday</i></span><span>Четверг<i>Thursday</i></span><span>Пятница<i>Friday</i></span><span>Суббота<i>Saturday</i></span><span>Воскресенье<i>Sunday</i></span></div>
      <div class="rows">
        <div class="row"><span class="wk">05</span><span class="other">27</span><span class="other">28</span><span class="other">29</span><span class="other">30</span><span class="other">31</span><span class="off">1</span><span class="off">2</span></div>
        <div class="row"><span class="wk">06</span><span>3</span><span>4</span><span>5</span><span>6</span><span>7</span><span class="off">8</span><span class="off">9</span></div>
        <div class="row"><span class="wk">07</span><span>10</span><span>11</span><span>12</span><span>13</span><span>14</span><span class="off">15</span><span class="off">16</span></div>
        <div class="row"><span class="wk">08</span><span>17</span><span>18</span><span>19</span><span>20</span><span>21</span><span class="off">22</span><span class="off">23</span></div>
        <div class="row"><span class="wk">09</span><span>24</span><span>25</span><span>26</span><span>27</span><span>28</span><span class="next">1</span><span class="next">2</span></div>
      </div>
    </div>
  </section>

  <div class="footer-info">
    ООО «ДОМ ЛИСТОВ»<br>
    Телефон: +7 (916) 457-31-09<br>
    E-mail: mv@listodom-studio.ru<br>
    129344, г. Москва, Зелёный 5-й переулок,<br>
    дом 17, строение 2, офис 14
  </div>
  <div class="studio">
    <div class="mark"></div>
    <div class="name">ДОМ ЛИСТОВ<span class="tag">ТИПОГРАФИЯ</span></div>
  </div>
</div>
</body>
</html>
```